Redesign Our Presentation on Rational Prescribing

We are looking for a new designer for QVMed, a project that creates educational modules for healthcare providers in the District of Columbia (more information at hlb.example-gov.org/qvmed). We want someone to redesign our powerpoints to look clean and professional, with original graphics that reflect the content on the slides. We also want someone who is creative and could potentially also redesign factsheets, written reports, and promotional postcards.

All the text on the slides must stay the same and it must be in the template (red line at the top, with the red box at the bottom, with the Harlow Bureau of Wellness logo). We want a powerpoint that features original graphics, looks professional, looks clean and is easy to read.

Industry/Entity Type

Healthcare

```html
<!DOCTYPE html>
<html lang="en">
<head>
<meta charset="utf-8">
<title>QVMed – Rational Prescribing Deck</title>
<link rel="stylesheet" href="https://fonts.googleapis.com/css2?family=Open+Sans:wght@400;600;700&display=swap">
<style>
:root{
  --navy:#2b2d6e;
  --navy-deep:#1f2258;
  --red:#e5262e;
  --ink:#3b3b48;
  --muted:#8a8a94;
  --band:#e2e2e4;
  --bubble:#b9b9bd;
  --shelf:#c9c9cc;
  --canvas:#6c6c6c;
  --white:#ffffff;
}
*{box-sizing:border-box}
html,body{margin:0;padding:0}
body{width:1200px;height:887px;overflow:hidden;background:var(--canvas);font-family:'Open Sans',sans-serif;position:relative}
.slide{position:absolute;width:348px;height:192px;background:var(--white);overflow:hidden}
.slide-title{position:absolute;left:20px;top:15px;margin:0;font-size:8.5px;font-weight:400;color:var(--navy);letter-spacing:.3px;text-transform:uppercase}
.brand{position:absolute;right:10px;top:7px;display:flex;align-items:center;gap:3px;color:var(--navy);font-size:5.6px;font-weight:700;line-height:1.15}
.brand-mark{width:7px;height:7px;background:var(--navy)}
.header-rule{position:absolute;left:0;right:0;top:33px;height:1px;background:var(--red)}
.slide-footer{position:absolute;left:0;right:0;bottom:0;height:16px}
.footer-rule{position:absolute;left:0;right:0;bottom:5px;height:1px;background:var(--red)}
.page-num{position:absolute;left:14px;bottom:7px;font-size:4px;color:var(--muted)}
.site{position:absolute;right:10px;bottom:0;width:80px;height:11px;background:var(--red);color:var(--white);font-size:5px;line-height:11px;text-align:center}
.art{position:absolute;left:0;top:0;width:348px;height:192px}
.art text{font-family:'Open Sans',sans-serif}
.copy{position:absolute;margin:0;font-size:4.5px;line-height:1.38;color:var(--ink)}
.copy ul{margin:1px 0 0;padding-left:7px}
.copy li{margin-bottom:1px}
.strong{font-weight:700;color:var(--navy)}
.center{text-align:center}

/* best drugs */
.step-text{position:absolute;top:90px;width:72px;font-size:5.6px;line-height:1.35;color:var(--ink);margin:0}
.step-text small{display:block;font-size:4.3px;margin-top:2px}

/* antipsychotics */
.bubble{position:absolute;top:44px;width:56px;height:38px;border-radius:50% 50% 50% 10%;color:var(--white);font-size:4.3px;line-height:1.3;display:flex;align-items:center;justify-content:center;text-align:center;padding:6px}
.bubble.navy{background:var(--navy)}
.bubble.red{background:var(--red)}
.bubble-num{position:absolute;top:40px;width:12px;height:12px;border-radius:50%;background:var(--white);border:1px solid var(--navy);font-size:4.5px;line-height:10px;text-align:center;color:var(--navy)}

/* generations */
.gen-head{position:absolute;top:60px;margin:0;font-size:6px;font-weight:600;color:var(--red);text-decoration:underline}

/* case study choices */
.choice{position:absolute;font-size:4.2px;line-height:1.3;color:var(--white);padding:3px 4px;margin:0}
.choice.navy{background:var(--navy)}
.choice.red{background:var(--red)}
.choice-tag{position:absolute;width:14px;height:12px;font-size:5px;font-weight:700;line-height:10px;text-align:center;border:1px solid}
.choice-tag.navy{color:var(--navy);border-color:var(--navy);background:var(--white)}
.choice-tag.red{color:var(--white);border-color:var(--red);background:var(--red)}

/* chevrons */
.chevron-row{position:absolute;left:26px;top:92px;display:flex}
.chevron{width:78px;height:30px;color:var(--white);font-size:5.4px;line-height:1.25;display:flex;align-items:center;justify-content:center;text-align:center;padding:0 12px 0 14px;margin-left:-6px;clip-path:polygon(0 0,calc(100% - 10px) 0,100% 50%,calc(100% - 10px) 100%,0 100%,10px 50%)}
.chevron:first-child{margin-left:0;padding-left:6px;clip-path:polygon(0 0,calc(100% - 10px) 0,100% 50%,calc(100% - 10px) 100%,0 100%)}
.chevron.navy{background:var(--navy)}
.chevron.red{background:var(--red)}

/* resources */
.lead{position:absolute;left:30px;top:62px;width:135px;margin:0;font-size:8.6px;line-height:1.35;color:var(--ink)}
.shelf{position:absolute;left:0;right:0;top:122px;height:12px;background:var(--shelf)}
.ribbon{position:absolute;width:20px;bottom:42px;color:var(--white);font-size:6px;display:flex;flex-direction:column;justify-content:flex-start;align-items:center;padding-top:12px;clip-path:polygon(50% 0,100% 8px,100% 100%,0 100%,0 8px)}
.ribbon span{writing-mode:vertical-rl;transform:rotate(180deg);white-space:nowrap;line-height:20px}
.ribbon.navy{background:var(--navy)}
.ribbon.red{background:var(--red)}
.ribbon-num{position:absolute;bottom:22px;width:20px;height:18px;color:var(--white);font-size:5.5px;line-height:18px;text-align:center}
.ribbon-num.navy{background:var(--navy)}
.ribbon-num.red{background:var(--red)}
</style>
</head>
<body>

<!-- Slide 2: Consequences -->
<section class="slide" style="left:48px;top:38px">
  <h2 class="slide-title">Consequences of multiple medication use</h2>
  <div class="brand"><span class="brand-mark"></span><span>Harlow Bureau<br>of Wellness</span></div>
  <div class="header-rule"></div>
  <svg class="art" viewBox="0 0 348 192" aria-hidden="true">
    <rect x="70" y="85" width="262" height="13" fill="var(--band)"/>
    <rect x="80" y="107" width="252" height="14" fill="var(--band)"/>
    <rect x="90" y="131" width="242" height="20" fill="var(--band)"/>
    <polygon points="68,40 85.6,80 50.4,80" fill="var(--navy)"/>
    <polygon points="70,58 76,62 70,66" fill="var(--white)"/>
    <polygon points="49.1,83 86.9,83 94.4,100 41.6,100" fill="var(--red)"/>
    <polygon points="40.3,103 95.7,103 104.5,123 31.5,123" fill="var(--navy)"/>
    <polygon points="29.7,127 106.3,127 123,165 13,165" fill="var(--red)"/>
    <text x="68" y="95" font-size="7" font-weight="700" fill="#fff" text-anchor="middle">13%</text>
    <text x="68" y="117" font-size="8" font-weight="700" fill="#fff" text-anchor="middle">58%</text>
    <text x="68" y="150" font-size="9" font-weight="700" fill="#fff" text-anchor="middle">82%</text>
  </svg>
  <p class="copy" style="left:150px;top:46px;width:180px">The use of several medications simultaneously, even at otherwise appropriate doses, increases the risk of adverse effects, drug interactions, non-adherence, and death.</p>
  <p class="copy" style="left:135px;top:88px">The risk of ADRs when taking two medicines</p>
  <p class="copy" style="left:135px;top:111px">The risk of ADRs when taking five medicines is</p>
  <p class="copy" style="left:135px;top:133px">The risk of ADRs when taking seven medicines<br>(Dawes 2015)</p>
  <footer class="slide-footer"><div class="footer-rule"></div><span class="page-num">2</span><span class="site">www.hlb.example-gov.org</span></footer>
</section>

<!-- Slide 3: Predicting ADRs -->
<section class="slide" style="left:446px;top:38px">
  <h2 class="slide-title">Predicting ADRs</h2>
  <div class="brand"><span class="brand-mark"></span><span>Harlow Bureau<br>of Wellness</span></div>
  <div class="header-rule"></div>
  <svg class="art" viewBox="0 0 348 192" aria-hidden="true">
    <circle cx="26" cy="53" r="10" fill="none" stroke="var(--navy)" stroke-width="1.2"/>
    <text x="26" y="55.5" font-size="7" fill="var(--navy)" text-anchor="middle">01</text>
    <circle cx="26" cy="88" r="10" fill="var(--red)"/>
    <circle cx="26" cy="88" r="7.5" fill="none" stroke="#fff" stroke-width=".8"/>
    <text x="26" y="90.5" font-size="7" fill="#fff" text-anchor="middle">02</text>
    <circle cx="26" cy="128" r="10" fill="none" stroke="var(--navy)" stroke-width="1.2"/>
    <text x="26" y="130.5" font-size="7" fill="var(--navy)" text-anchor="middle">03</text>
  </svg>
  <p class="copy" style="left:48px;top:50px;width:285px">Few ADRs represent improper prescribing</p>
  <p class="copy" style="left:48px;top:78px;width:285px">Most ADRs are related to the pharmacologic properties of a drug. <b>(For eg.</b> Benzodiazepines cause increased imbalance and gait instability associated with increased risk of falls. A patient taking a nightly benzodiazepine to induce sleep is at high risk for falls. All subsequent health care costs and associated disability are due to the prescribed medication)</p>
  <p class="copy" style="left:48px;top:112px;width:285px">Many ADRs are both predictable and avoidable (Dawes &amp; Malory 2015) <b>(For eg.</b> Anticholinergic medications prescribed to control bladder spasm may result in constipation and even mental status changes. These are expected outcomes from modulating acetylcholine levels. This type of drug associated adverse effect raises the risk of prescribing additional medications, such as constipation relieving agents, to address adverse effects of the original drug. Eliminating, changing, or lowering the dose of the original drug is the right course of action.</p>
  <footer class="slide-footer"><div class="footer-rule"></div><span class="page-num">3</span><span class="site">www.hlb.example-gov.org</span></footer>
</section>

<!-- Slide 4: Drug classes -->
<section class="slide" style="left:818px;top:38px">
  <h2 class="slide-title">Drug classes most commonly involved in ADRs</h2>
  <div class="brand"><span class="brand-mark"></span><span>Harlow Bureau<br>of Wellness</span></div>
  <div class="header-rule"></div>
  <svg class="art" viewBox="0 0 348 192" aria-hidden="true">
    <rect x="10" y="45" width="38" height="28" fill="var(--navy)"/>
    <rect x="10" y="75" width="38" height="28" fill="var(--red)"/>
    <rect x="10" y="105" width="38" height="28" fill="var(--navy)"/>
    <rect x="10" y="135" width="38" height="28" fill="var(--red)"/>
    <text x="29" y="62" font-size="7" fill="#fff" text-anchor="middle">01</text>
    <text x="29" y="92" font-size="7" fill="#fff" text-anchor="middle">02</text>
    <text x="29" y="122" font-size="7" fill="#fff" text-anchor="middle">03</text>
    <text x="29" y="152" font-size="7" fill="#fff" text-anchor="middle">04</text>
    <polygon points="48,45 300,45 322,86 300,127 48,127" fill="var(--navy)"/>
    <text x="105" y="64" font-size="9.5" fill="#fff">ADRs during hospitalization</text>
    <polygon points="60,74 252,74 259,80 252,86 60,86" fill="var(--red)"/>
    <text x="110" y="82" font-size="5" fill="#fff">Cardiovascular agents</text>
    <text x="270" y="84" font-size="10" font-weight="700" fill="#fff">34%</text>
    <polygon points="60,91 252,91 259,97 252,103 60,103" fill="var(--red)"/>
    <text x="110" y="99" font-size="5" fill="#fff">Analgesic medications</text>
    <text x="270" y="101" font-size="10" font-weight="700" fill="#fff">18%</text>
    <polygon points="60,108 252,108 259,114 252,120 60,120" fill="var(--navy-deep)"/>
    <text x="110" y="116" font-size="5" fill="#fff">Anti-diabetic drugs</text>
    <text x="270" y="118" font-size="10" font-weight="700" fill="#fff">10%</text>
    <polygon points="48,131 290,131 304,147 290,163 48,163" fill="var(--red)"/>
    <text x="314" y="140" font-size="7" font-weight="700" fill="var(--navy)" text-anchor="middle">Tanaveri</text>
    <text x="314" y="149" font-size="7" font-weight="700" fill="var(--navy)" text-anchor="middle">2012</text>
  </svg>
  <p class="copy" style="left:56px;top:135px;width:225px;color:#fff">Predictors of ADRs included the number of medications, use of hypoglycaemic agents, history of hyperglycaemia, neutrophil count on admission and length of stay.</p>
  <footer class="slide-footer"><div class="footer-rule"></div><span class="page-num">4</span><span class="site">www.hlb.example-gov.org</span></footer>
</section>

<!-- Slide 5: Best drugs -->
<section class="slide" style="left:48px;top:237px">
  <h2 class="slide-title">Best drugs in diabetic elders</h2>
  <div class="brand"><span class="brand-mark"></span><span>Harlow Bureau<br>of Wellness</span></div>
  <div class="header-rule"></div>
  <svg class="art" viewBox="0 0 348 192" aria-hidden="true">
    <line x1="18" y1="72" x2="332" y2="72" stroke="#c4c4c8" stroke-width="1"/>
    <circle cx="48" cy="72" r="7" fill="var(--navy)"/>
    <circle cx="132" cy="72" r="7" fill="var(--red)"/>
    <circle cx="214" cy="72" r="7" fill="var(--navy)"/>
    <circle cx="296" cy="72" r="7" fill="var(--red)"/>
    <text x="48" y="74" font-size="5.5" fill="#fff" text-anchor="middle">01</text>
    <text x="132" y="74" font-size="5.5" fill="#fff" text-anchor="middle">02</text>
    <text x="214" y="74" font-size="5.5" fill="#fff" text-anchor="middle">03</text>
    <text x="296" y="74" font-size="5.5" fill="#fff" text-anchor="middle">04</text>
  </svg>
  <p class="step-text" style="left:20px">Only metformin should be used to achieve hemoglobin A1c &lt; 7.5% in most older adults with type 2 diabetes.</p>
  <p class="step-text" style="left:112px">Avoid insulin!</p>
  <p class="step-text" style="left:185px">Insulin-related hypoglycemia and errors are implicated in an estimated 9.2% of ED visits associated with ADE (Garner et al 2014)</p>
  <p class="step-text" style="left:264px">This one preventable ADE accounts for nearly 100,000 ED Visits every year.<small>&gt; Patients at or above the age of 80 were twice as likely to visit the ED and 5 times more likely to be hospitalized.</small></p>
  <footer class="slide-footer"><div class="footer-rule"></div><span class="page-num">5</span><span class="site">www.hlb.example-gov.org</span></footer>
</section>

<!-- Slide 6: Antipsychotics -->
<section class="slide" style="left:446px;top:237px">
  <h2 class="slide-title">Antipsychotics</h2>
  <div class="brand"><span class="brand-mark"></span><span>Harlow Bureau<br>of Wellness</span></div>
  <div class="header-rule"></div>
  <div class="bubble navy" style="left:26px">Antipsychotics should NOT be the first choice</div>
  <div class="bubble red" style="left:122px">Risks of antipsychotics include</div>
  <div class="bubble navy" style="left:256px">Antipsychotics may actually increase delirium</div>
  <span class="bubble-num" style="left:22px">01</span>
  <span class="bubble-num" style="left:118px">02</span>
  <span class="bubble-num" style="left:252px">03</span>
  <p class="copy" style="left:22px;top:90px;width:80px">Antipsychotics should NOT be the first choice to treat behavioral and psychological symptoms of dementia.</p>
  <div class="copy" style="left:118px;top:86px;width:110px;font-size:4.2px">
    <ul>
      <li>Death</li><li>Strokes</li><li>Diabetes</li><li>Weight gain</li><li>Cognitive decline</li>
      <li>Neuroleptic malignant syndrome (fever, autonomic instability, altered mental state and extrapyramidal signs)</li>
      <li>Extrapyramidal effects</li><li>Hypothermia</li><li>Oversedation</li><li>Falls</li>
    </ul>
  </div>
  <p class="copy" style="left:254px;top:90px;width:80px">REVIEWERS: Original statement here only lorazepam and haloperidol. Should we list other drugs that can cause delirium?</p>
  <footer class="slide-footer"><div class="footer-rule"></div><span class="page-num">6</span><span class="site">www.hlb.example-gov.org</span></footer>
</section>

<!-- Slide 7: Death -->
<section class="slide" style="left:818px;top:237px">
  <h2 class="slide-title">Death</h2>
  <div class="brand"><span class="brand-mark"></span><span>Harlow Bureau<br>of Wellness</span></div>
  <div class="header-rule"></div>
  <svg class="art" viewBox="0 0 348 192" aria-hidden="true">
    <defs>
      <path id="petal" d="M0,-5 C-5,-10 -9,-15 -9,-20 A9,9 0 1 1 9,-20 C9,-15 5,-10 0,-5Z"/>
    </defs>
    <use href="#petal" fill="var(--navy)" transform="translate(172,100) rotate(-36)"/>
    <use href="#petal" fill="var(--navy)" transform="translate(172,100) rotate(36)"/>
    <use href="#petal" fill="var(--red)" transform="translate(172,100) rotate(108)"/>
    <use href="#petal" fill="var(--red)" transform="translate(172,100) rotate(180)"/>
    <use href="#petal" fill="var(--red)" transform="translate(172,100) rotate(-108)"/>
    <text x="157.4" y="82" font-size="6.5" fill="#fff" text-anchor="middle">01</text>
    <text x="186.6" y="82" font-size="6.5" fill="#fff" text-anchor="middle">05</text>
    <text x="196" y="109" font-size="6.5" fill="#fff" text-anchor="middle">04</text>
    <text x="172" y="126" font-size="6.5" fill="#fff" text-anchor="middle">03</text>
    <text x="148" y="109" font-size="6.5" fill="#fff" text-anchor="middle">02</text>
  </svg>
  <p class="copy center" style="left:68px;top:58px;width:78px">Antipsychotics increase mortality</p>
  <p class="copy" style="left:200px;top:55px;width:125px">Antipsychotics carry a black box warning for increased death rates in elders.</p>
  <p class="copy center" style="left:14px;top:88px;width:120px">The mechanism may be abnormal heart rhythms; antipsychotics double the risk of sudden cardiac death. <b>(Vierling 2008 impacts)</b></p>
  <p class="copy center" style="left:208px;top:88px;width:125px">The number needed to harm is 87, meaning that one in 87 patients treated with antipsychotics can be expected to die from the treatment <b>(Maddox 2011 impacts)</b></p>
  <p class="copy center" style="left:105px;top:136px;width:140px">A systematic review and meta-analysis of 102 studies found that deaths occurred in 3.5% of patients randomized to SGAs compared to 2.3% of those randomized to placebo (OR 1.54 (95% CI 1.06-2.23). <b>(Maddox 2011 impacts)</b></p>
  <footer class="slide-footer"><div class="footer-rule"></div><span class="page-num">7</span><span class="site">www.hlb.example-gov.org</span></footer>
</section>

<!-- Slide 8: Generations -->
<section class="slide" style="left:48px;top:437px">
  <h2 class="slide-title">“Second generation” vs. “First generation”</h2>
  <div class="brand"><span class="brand-mark"></span><span>Harlow Bureau<br>of Wellness</span></div>
  <div class="header-rule"></div>
  <p class="copy strong center" style="left:14px;top:44px;width:320px;font-size:5px">There is no advantage to so-called “second generation” antipsychotics over “first generation” antipsychotics.</p>
  <h3 class="gen-head" style="left:24px">first generation</h3>
  <h3 class="gen-head" style="left:210px">second generation</h3>
  <svg class="art" viewBox="0 0 348 192" aria-hidden="true">
    <polygon points="128,80 188,80 188,74 204,87 188,100 188,94 128,94" fill="var(--navy)"/>
    <text x="160" y="89" font-size="5" fill="#fff" text-anchor="middle">second generation</text>
    <polygon points="184,100 126,100 126,94 110,107 126,120 126,114 184,114" fill="var(--red)"/>
    <text x="152" y="109" font-size="5" fill="#fff" text-anchor="middle">first generation</text>
  </svg>
  <div class="copy" style="left:24px;top:72px;width:80px;font-size:4.2px">“First generation” antipsychotics are just as effective as so-called “second generation” antipsychotics.
    <ul>
      <li>The Federally funded CATIE study found that haloperidol (Halvex) was just as effective as so-called “second generation” antipsychotics (Castell 2007 impacts)</li>
      <li>The CATIE study made no difference in the sales of SGAs.</li>
    </ul>
  </div>
  <div class="copy" style="left:210px;top:70px;width:124px;font-size:4.2px">
    <ul>
      <li>The term “second generation” was developed for marketing purposes.</li>
      <li>“Second generation” antipsychotics do not have fewer adverse effects. Although sold as less likely to cause tardive dyskinesia, “second generation” antipsychotics are just as likely as “first generation” antipsychotics to cause tardive dyskinesia and other extrapyramidal symptoms (Pelham impacts)</li>
    </ul>
  </div>
  <footer class="slide-footer"><div class="footer-rule"></div><span class="page-num">8</span><span class="site">www.hlb.example-gov.org</span></footer>
</section>

<!-- Slide 9: Case study intro -->
<section class="slide" style="left:446px;top:437px">
  <h2 class="slide-title">Case study 3 - Insomnia</h2>
  <div class="brand"><span class="brand-mark"></span><span>Harlow Bureau<br>of Wellness</span></div>
  <div class="header-rule"></div>
  <p class="copy" style="left:20px;top:46px;width:112px;text-align:justify">A 79 yo female presents to clinic for general follow-up. On a comprehensive medication review, you identify that she is taking “Somnel” occasionally (an over the counter sleep aid containing diphenhydramine) and lorazepam each night prior to bedtime. She reports that she has taken the lorazepam “as long as I can remember” and uses the Somnel to help her sleep through the night.</p>
  <svg class="art" viewBox="0 0 348 192" aria-hidden="true">
    <g transform="rotate(-30 172 100)">
      <circle cx="172" cy="100" r="27" fill="none" stroke="var(--red)" stroke-width="13"/>
      <path d="M145,100 A27,27 0 0 1 199,100" fill="none" stroke="var(--navy)" stroke-width="13"/>
      <text x="172" y="79" font-size="6" font-weight="600" fill="#fff" text-anchor="middle">Case Study</text>
      <text x="172" y="126" font-size="6" font-weight="600" fill="#fff" text-anchor="middle">Case Study</text>
    </g>
  </svg>
  <p class="copy" style="left:214px;top:64px;width:120px;text-align:justify">On further questioning, you learn that she has some anxiety in the evenings and started taking lorazepam decades ago when her late husband became ill. Now she is often able to go to sleep, but wakes up several times nightly to urinate. She finds the Somnel helps her stay asleep through the night.</p>
  <footer class="slide-footer"><div class="footer-rule"></div><span class="page-num">9</span><span class="site">www.hlb.example-gov.org</span></footer>
</section>

<!-- Slide 10: Case study choices -->
<section class="slide" style="left:818px;top:437px">
  <h2 class="slide-title">Case study 3 - Insomnia</h2>
  <div class="brand"><span class="brand-mark"></span><span>Harlow Bureau<br>of Wellness</span></div>
  <div class="header-rule"></div>
  <p class="copy strong center" style="left:0;top:40px;width:348px;font-size:6.5px">What would you do?</p>
  <svg class="art" viewBox="0 0 348 192" aria-hidden="true">
    <line x1="175" y1="52" x2="175" y2="165" stroke="#c4c4c8" stroke-width="1"/>
  </svg>
  <span class="choice-tag navy" style="left:178px;top:58px">(A)</span>
  <span class="choice-tag red" style="left:158px;top:80px">(B)</span>
  <span class="choice-tag navy" style="left:178px;top:102px">(C)</span>
  <span class="choice-tag red" style="left:158px;top:126px">(D)</span>
  <p class="choice navy" style="left:62px;top:56px;width:100px">Continue lorazepam, she has had no adverse effects thus far, discontinue Somnel.</p>
  <p class="choice red" style="left:194px;top:74px;width:110px">Discontinue both medications immediately – their risk profiles outweigh any continued benefit.</p>
  <p class="choice navy" style="left:30px;top:100px;width:124px">Discontinue both medications, and instead prescribe a newer sleep aid like zolpidem. You know that benzodiazepines are bad.</p>
  <p class="choice red" style="left:194px;top:122px;width:140px">Initiate taper off of lorazepam and stop Somnel. Discuss sleep hygiene, modifying therapies to decrease nocturia and consider CBT if nocturnal anxiety returns.</p>
  <footer class="slide-footer"><div class="footer-rule"></div><span class="page-num">10</span><span class="site">www.hlb.example-gov.org</span></footer>
</section>

<!-- Slide 11: Non-pharmacological -->
<section class="slide" style="left:48px;top:640px">
  <h2 class="slide-title">Non-pharmacological options to recommend</h2>
  <div class="brand"><span class="brand-mark"></span><span>Harlow Bureau<br>of Wellness</span></div>
  <div class="header-rule"></div>
  <div class="chevron-row">
    <div class="chevron navy">Try a hot bath before bedtime</div>
    <div class="chevron red">Try strong chamomile tea (made with three teabags)</div>
    <div class="chevron navy">Try meditation or relaxation tapes</div>
    <div class="chevron red">Other?</div>
  </div>
  <footer class="slide-footer"><div class="footer-rule"></div><span class="page-num">11</span><span class="site">www.hlb.example-gov.org</span></footer>
</section>

<!-- Slide 12: Medication reconciliation -->
<section class="slide" style="left:446px;top:640px">
  <h2 class="slide-title">Medication reconciliation</h2>
  <div class="brand"><span class="brand-mark"></span><span>Harlow Bureau<br>of Wellness</span></div>
  <div class="header-rule"></div>
  <svg class="art" viewBox="0 0 348 192" aria-hidden="true">
    <g stroke="#b0b0b6" stroke-width=".8">
      <line x1="70" y1="86" x2="100" y2="58"/>
      <line x1="76" y1="96" x2="112" y2="80"/>
      <line x1="76" y1="106" x2="112" y2="108"/>
      <line x1="70" y1="116" x2="100" y2="132"/>
    </g>
    <circle cx="50" cy="101" r="26" fill="var(--bubble)"/>
    <circle cx="100" cy="58" r="7" fill="var(--navy)"/>
    <circle cx="112" cy="80" r="7" fill="var(--red)"/>
    <circle cx="112" cy="108" r="7" fill="var(--navy)"/>
    <circle cx="100" cy="132" r="7" fill="var(--red)"/>
    <g fill="none" stroke="#fff" stroke-width="1.2">
      <polyline points="98,55 101.5,58 98,61"/>
      <polyline points="110,77 113.5,80 110,83"/>
      <polyline points="110,105 113.5,108 110,111"/>
      <polyline points="98,129 101.5,132 98,135"/>
    </g>
  </svg>
  <p class="copy center" style="left:30px;top:88px;width:40px;color:var(--navy)">What pharmaceuticals should be discontinued? Pharmaceuticals where.</p>
  <p class="copy" style="left:126px;top:50px;width:205px">Medication reconciliation process should be completed universally and regularly.</p>
  <p class="copy" style="left:126px;top:73px;width:205px;font-weight:700">Formal medication reviews at the time of discharge from the hospital (for patients with ten or more medications) or on a regular basis for outpatients.</p>
  <p class="copy" style="left:126px;top:102px;width:205px">What medications are being used? What medications are being prescribed but not being used?</p>
  <p class="copy" style="left:126px;top:126px;width:205px">To get honest answers, use non-accusatory language: “In the past month, how many doses of this medication did you take?”</p>
  <footer class="slide-footer"><div class="footer-rule"></div><span class="page-num">12</span><span class="site">www.hlb.example-gov.org</span></footer>
</section>

<!-- Slide 13: Resources -->
<section class="slide" style="left:818px;top:640px">
  <h2 class="slide-title">Resources</h2>
  <div class="brand"><span class="brand-mark"></span><span>Harlow Bureau<br>of Wellness</span></div>
  <div class="header-rule"></div>
  <p class="lead">Utilize non-commercial research to inform your prescribing preferences.</p>
  <div class="shelf"></div>
  <div class="ribbon red" style="left:178px;top:58px"><span>Rx Review</span></div>
  <div class="ribbon red" style="left:204px;top:68px"><span>Therapy Letter</span></div>
  <div class="ribbon navy" style="left:232px;top:48px"><span>Prescribers Brief</span></div>
  <div class="ribbon red" style="left:258px;top:52px"><span>Evidence Now</span></div>
  <span class="ribbon-num navy" style="left:178px">01</span>
  <span class="ribbon-num red" style="left:204px">02</span>
  <span class="ribbon-num navy" style="left:232px">03</span>
  <span class="ribbon-num red" style="left:258px">04</span>
  <footer class="slide-footer"><div class="footer-rule"></div><span class="page-num">13</span><span class="site">www.hlb.example-gov.org</span></footer>
</section>

</body>
</html>
```